Stylish High End Wedding Videography/Films Website (BDMR)

We need a modern and high-end website look for our wedding video and films business. We films weddings all over the United Kingdom and at European destinations so need something to reflect our work. The website should be visually stunning with images and videos being the focal point as this is what our services are;

I have uploads of some items I like and the features the site needs to have. These have been taken from other websites using standout features.

We need the following pages;

1 - Homepage
2 - Films Index Page
3 - Individual Films Page
4 - Prices / Collection Page
5 - Reviews
6 - Options
7 - About
8 - Contact
9 - Blog Index
10 - Blog Page

All pages must be consistent so have a similar style.

Pages on menu:
Films
Prices
Reviews
Options
About
Contact

We require a responsive look too. Over 90% of our visitors access the website via their mobile devices.

Please use the colours from our logo to incorporate into the website.

Target Market(s)

Wedding Couples

Industry/Entity Type

Wedding Photography

Number of Pages Required

5+ page

Font styles to use
Sans Serif
Script

Requirements
Must have
• The logo must be in the centre of the menu at the top.

Social icons at the bottom of the page.

Use only two fonts including Lore which is supplied
Nice to have
• Different video for each page on the top header. This will play behind the menu.

```html
<!DOCTYPE html>
<html lang="en">
<head>
<meta charset="utf-8">
<title>BDMR Wedding Films</title>
<link href="https://fonts.googleapis.com/css2?family=Josefin+Sans:wght@300;400;600&family=Jost:wght@400;500&display=swap" rel="stylesheet">
<style>
:root{
  --gold:#a88f52;
  --gold-text:#a0894c;
  --ink:#2a2a2a;
  --body:#4a4a4a;
  --white:#ffffff;
  --footer:#3b332d;
  --dark-panel:#2b2b2b;
}
*{box-sizing:border-box;margin:0;padding:0}
html,body{width:1200px;height:5348px;overflow:hidden}
body{position:relative;background:var(--white);font-family:"Josefin Sans",sans-serif;color:var(--body)}
.abs{position:absolute}
.photo{position:absolute}
.center{left:0;width:1200px;text-align:center}
.heading-kicker{font-family:"Jost",sans-serif;font-size:17px;letter-spacing:6px;color:var(--gold-text);text-transform:uppercase}
.heading-main{font-family:"Jost",sans-serif;font-size:29px;letter-spacing:10px;color:var(--ink);text-transform:uppercase;font-weight:500}
.btn{position:absolute;border:2px solid var(--gold);color:var(--gold-text);font-size:12px;letter-spacing:4px;text-transform:uppercase;display:flex;align-items:center;justify-content:center;font-family:"Jost",sans-serif}
.play{position:absolute}

/* hero */
.hero{left:0;top:0;width:1200px;height:754px;background:radial-gradient(ellipse at 55% 55%,#6b5a45 0%,#3a3026 40%,#1d1914 100%)}
.nav-item{position:absolute;top:68px;font-size:11px;letter-spacing:2px;color:var(--white);text-transform:uppercase}
.brand{position:absolute;top:78px;left:0;width:1200px;text-align:center;color:var(--white);font-family:"Jost",sans-serif}
.brand-name{font-size:18px;letter-spacing:5px;font-weight:500}
.brand-sub{font-size:8px;letter-spacing:5px;margin-top:3px}
.hero-title{top:306px;color:var(--white);font-size:29px;line-height:45px;font-weight:400}

/* intro band */
.intro{left:0;top:754px;width:1200px;height:321px;background:var(--gold)}
.intro-mark{top:82px;color:var(--white);font-family:"Jost",sans-serif;font-size:26px;letter-spacing:6px}
.intro-text{top:140px;color:var(--white);font-size:11px;line-height:30px;text-transform:uppercase;letter-spacing:.3px}

/* portfolio */
.portfolio-grid{left:0;top:1254px;width:1200px;height:803px;display:grid;grid-template-columns:repeat(3,400px);grid-template-rows:402px 401px}
.film-tile{position:relative}
.film-couple{position:absolute;bottom:48px;width:100%;text-align:center;color:var(--white);font-family:"Jost",sans-serif;font-size:17px;letter-spacing:8px}
.film-venue{position:absolute;bottom:24px;width:100%;text-align:center;color:var(--white);font-size:10px;text-transform:uppercase}

/* about */
.about-portrait{left:0;top:2308px;width:440px;height:414px;background:linear-gradient(90deg,#7a6a5d 0%,#4d433c 45%,var(--dark-panel) 70%)}
.about-video{left:297px;top:2408px;width:299px;height:208px;background:linear-gradient(135deg,#c9362d 0%,#e8dcc8 45%,#c23a2f 75%,#8a2a24 100%);box-shadow:0 6px 18px rgba(0,0,0,.35)}
.about-copy{left:648px;top:2298px;width:470px}
.about-copy p{font-size:10.5px;line-height:30px;text-transform:uppercase;color:var(--body);margin-top:14px}

/* funky */
.funky-title{top:2956px;font-family:"Jost",sans-serif;font-size:28px;letter-spacing:9px;color:var(--ink);font-weight:500}
.funky-sub{top:3022px;font-size:11px;text-transform:uppercase}
.funky-photo{left:0;top:3170px;width:1200px;height:594px;background:linear-gradient(180deg,#e6e6e4 0%,#bdbdbb 30%,#8c8c8a 52%,#3e3e3d 68%,#1f1f1f 100%)}

/* reviews */
.review-thumb{top:3969px;width:474px;height:256px}
.review-name{top:4266px;font-family:"Jost",sans-serif;font-size:22px;letter-spacing:6px;color:var(--ink)}
.review-place{top:4306px;font-size:12px;letter-spacing:4px;color:var(--gold-text);text-transform:uppercase}
.review-text{top:4346px;width:470px;font-size:10.5px;line-height:30px;text-transform:uppercase}
.review-text p+p{margin-top:0}

/* social band */
.social-band{left:0;top:4661px;width:1200px;height:176px;background:var(--gold)}
.social-kicker{top:4722px;color:var(--white);font-family:"Jost",sans-serif;font-size:16px;letter-spacing:6px}
.social-main{top:4748px;color:var(--white);font-family:"Jost",sans-serif;font-size:28px;letter-spacing:9px;font-weight:500}
.social-row{left:0;top:4837px;width:1200px;height:239px;display:grid;grid-template-columns:repeat(5,240px)}

/* footer */
.footer{left:0;top:5242px;width:1200px;height:106px;background:var(--footer)}
.footer-brand{left:88px;top:5290px;color:var(--gold);font-family:"Jost",sans-serif;font-size:18px;letter-spacing:3px}
.footer-copy{top:5298px;color:#d9d2c4;font-size:10px;text-transform:uppercase}
</style>
</head>
<body>

<!-- Hero -->
<section class="abs hero" role="img" aria-label="Bride and groom embracing under string lights at an evening reception"></section>
<nav>
  <span class="nav-item" style="left:83px">About</span>
  <span class="nav-item" style="left:197px">Films</span>
  <span class="nav-item" style="left:305px">Options</span>
  <span class="nav-item" style="left:808px">Reviews</span>
  <span class="nav-item" style="left:936px">Prices</span>
  <span class="nav-item" style="left:1051px">Contact</span>
</nav>
<div class="brand">
  <div class="brand-name">BDMR</div>
  <div class="brand-sub">WEDDING FILMS</div>
</div>
<h1 class="abs center hero-title">WEDDING VIDEOGRAPHY -<br>NORTH EAST, UK AND WORLDWIDE FILMS</h1>
<svg class="play" style="left:566px;top:408px" width="72" height="72" viewBox="0 0 72 72"><circle cx="36" cy="36" r="33" fill="none" stroke="#fff" stroke-width="3"/><path d="M29 24 L50 36 L29 48 Z" fill="#fff"/></svg>

<!-- Intro -->
<section class="abs intro"></section>
<div class="abs center intro-mark" style="top:836px">BDMR</div>
<p class="abs center intro-text" style="top:888px">BDMR is a wedding filmmaker based in the North East of England. We film weddings in a fun and natural way.<br>All weddings are totally unique to the couple. If you are looking for a wedding film for your special day we'd love to<br>hear from you.</p>

<!-- Portfolio -->
<div class="abs center heading-kicker" style="top:1138px">BDMR</div>
<h2 class="abs center heading-main" style="top:1163px">Portfolio</h2>
<section class="abs portfolio-grid">
  <div class="film-tile" role="img" aria-label="Couple standing on a white porch" style="background:linear-gradient(135deg,#9a9a9a,#4a4a4a 60%,#2e2e2e)"><div class="film-couple">HANNAH + JAMES</div><div class="film-venue">Ashgrove Hall Wedding</div></div>
  <div class="film-tile" role="img" aria-label="Black and white church interior with bride and groom" style="background:linear-gradient(180deg,#8c8c8c,#5e5e5e 50%,#2f2f2f)"><div class="film-couple">SOPHIE + TOM</div><div class="film-venue">Fernleigh Abbey, Northumberland</div></div>
  <div class="film-tile" role="img" aria-label="Groom and bride with bouquet in soft light" style="background:linear-gradient(135deg,#2e3440,#5a5650 55%,#9a8a76)"><div class="film-couple">AMARA + LEO</div><div class="film-venue">Villa Montorso, Valle, Italy</div></div>
  <div class="film-tile" role="img" aria-label="Couple leaning foreheads together at golden hour" style="background:linear-gradient(135deg,#2c3028,#5e5a44 55%,#b39a6a)"><div class="film-couple">GRACE + OWEN</div><div class="film-venue">Bramley Manor, Leicestershire</div></div>
  <div class="film-tile" role="img" aria-label="Couple kissing in a warm lit room" style="background:linear-gradient(135deg,#5c5046,#8c7a66 50%,#3c3630)"><div class="film-couple">ELLA + RYAN</div><div class="film-venue">Oakridge Inn, Durham</div></div>
  <div class="film-tile" role="img" aria-label="Groom smiling with bride in flower crown" style="background:linear-gradient(135deg,#4c4a44,#7a6c5e 55%,#a07a70)"><div class="film-couple">CHLOE + SAM</div><div class="film-venue">Ios Island, Greece</div></div>
</section>
<div class="btn" style="left:494px;top:2132px;width:206px;height:60px">View More</div>

<!-- About -->
<section class="abs about-portrait" role="img" aria-label="Portrait of the filmmaker"></section>
<div class="abs about-video" role="img" aria-label="Film still of a child on a striped seaside chair"></div>
<svg class="play" style="left:419px;top:2485px" width="56" height="56" viewBox="0 0 56 56"><circle cx="28" cy="28" r="25" fill="none" stroke="#fff" stroke-width="3"/><path d="M22 18 L39 28 L22 38 Z" fill="#fff"/></svg>
<div class="abs about-copy">
  <div class="heading-kicker" style="font-size:16px">About</div>
  <h2 class="heading-main" style="font-size:28px;margin-top:6px">Daniel Mercer</h2>
  <p>I'm a filmmaker who loves documenting couples' most important day of their lives. Based in County Durham I film weddings mostly in the North East of England however regularly travel around the UK and Europe.</p>
  <p>I first picked up a video camera when I was 8 years old making home movies documenting family holidays and events and it led me onto gaining a degree in TV and radio production at university. After university I set up the very first community interest company (CIC) in the UK which led to many opportunities including launching social enterprise week at the Treasury in London.</p>
</div>
<div class="btn" style="left:648px;top:2750px;width:205px;height:61px">Read More</div>

<!-- Alternative -->
<h2 class="abs center funky-title">PREFER SOMETHING A BIT MORE FUNKY?</h2>
<p class="abs center funky-sub">If you are a couple who prefers something a bit different to the styles above then why not go for our alternative option.</p>
<section class="abs funky-photo" role="img" aria-label="Couple embracing on a black sand beach with sea stacks"></section>
<div class="btn" style="left:498px;top:3083px;width:206px;height:60px;background:rgba(255,255,255,.6)">Contact Us</div>

<!-- Reviews -->
<div class="abs center heading-kicker" style="top:3834px">Client's</div>
<h2 class="abs center heading-main" style="top:3861px">Reviews</h2>
<div class="abs review-thumb" role="img" aria-label="Couple beside a wedding car in the countryside" style="left:79px;background:linear-gradient(180deg,#c9d4dc,#7f8a74 50%,#4a4e46)"></div>
<div class="abs review-thumb" role="img" aria-label="Groom and bride holding bouquet" style="left:650px;background:linear-gradient(135deg,#2e3440,#5a5650 55%,#b8aa98)"></div>
<svg class="play" style="left:280px;top:4061px" width="72" height="72" viewBox="0 0 72 72"><circle cx="36" cy="36" r="33" fill="none" stroke="#fff" stroke-width="3"/><path d="M29 24 L50 36 L29 48 Z" fill="#fff"/></svg>
<svg class="play" style="left:843px;top:4061px" width="72" height="72" viewBox="0 0 72 72"><circle cx="36" cy="36" r="33" fill="none" stroke="#fff" stroke-width="3"/><path d="M29 24 L50 36 L29 48 Z" fill="#fff"/></svg>
<div class="abs review-name" style="left:77px">GRACE <span style="color:var(--gold)">+</span> OWEN</div>
<div class="abs review-place" style="left:77px">Bramley Manor, Leicestershire</div>
<div class="abs review-text" style="left:77px"><p>I have filmed some amazing weddings over the years. My main aim is to ensure that couples enjoy their day and that they take in the moments so they remember them. Our wedding films are almost secondary.</p><p>Here are some amazing words from brides, grooms and couples who we've been so lucky to share their big day with.</p></div>
<div class="abs review-name" style="left:651px">AMARA <span style="color:var(--gold)">+</span> LEO</div>
<div class="abs review-place" style="left:651px">Umbria, Italy</div>
<div class="abs review-text" style="left:651px"><p>Absolutely amazing videographer! What can we say, our short film captures our day perfectly and includes everything we wanted. Both Daniel and Martin were most professional and easy to work with on the day. They captured moments that I wouldn't have seen otherwise (like groom panicking beforehand). Would highly recommend!</p></div>
<svg class="abs" style="left:575px;top:4572px" width="52" height="24" viewBox="0 0 52 24"><path d="M7 1 L12 12 L7 23 L2 12Z" fill="var(--gold)"/><path d="M26 1 L31 12 L26 23 L21 12Z" fill="var(--gold)"/><path d="M45 1 L50 12 L45 23 L40 12Z" fill="var(--gold)"/></svg>

<!-- Social -->
<section class="abs social-band"></section>
<div class="abs center social-kicker">Follow on</div>
<h2 class="abs center social-main">SOCIAL</h2>
<section class="abs social-row">
  <div role="img" aria-label="Couple hugging by a lake" style="background:linear-gradient(135deg,#3a4450,#6a7680 60%,#2a2e32)"></div>
  <div role="img" aria-label="Bride and groom kissing" style="background:linear-gradient(135deg,#5a6470,#9aa0a4 55%,#4a4a4a)"></div>
  <div role="img" aria-label="Couple walking under lights" style="background:linear-gradient(135deg,#22303a,#5a4a3a 55%,#1c1c1c)"></div>
  <div role="img" aria-label="Floral arch by the sea" style="background:linear-gradient(180deg,#a8bccc,#6a8aa0 50%,#8a9a7a)"></div>
  <div role="img" aria-label="Groom in a suit" style="background:linear-gradient(135deg,#3a3a3a,#7a6a5e 55%,#c8c0b6)"></div>
</section>
<div class="btn" style="left:504px;top:5132px;width:208px;height:62px;gap:14px">
  <svg width="22" height="22" viewBox="0 0 22 22"><rect x="2" y="2" width="18" height="18" fill="var(--gold)"/></svg>
  <span>Follow Us</span>
</div>

<!-- Footer -->
<footer class="abs footer"></footer>
<div class="abs footer-brand">BDMR</div>
<p class="abs center footer-copy">Copyright © 2020 BDMR Wedding Films. All rights reserved.</p>
<svg class="abs" style="left:1036px;top:5294px" width="80" height="20" viewBox="0 0 80 20"><circle cx="8" cy="10" r="7" fill="var(--gold)"/><circle cx="40" cy="10" r="7" fill="var(--gold)"/><circle cx="72" cy="10" r="7" fill="var(--gold)"/></svg>

</body>
</html>
```